" Consultório médico focado em atendimentos particulares para rinoplastia (principal) e otoplastia - cirurgias estéticas da face . Proposta mais luxuosa, consultório para atendimento mais personalizado focado em estética. "

```html
<!DOCTYPE html>
<html lang="pt-BR">
<head>
<meta charset="UTF-8">
<title>Dra. Clara Mendes – Pasta</title>
<link rel="stylesheet" href="https://fonts.googleapis.com/css2?family=Cormorant+Garamond:wght@400&family=Montserrat:wght@400;500&display=swap">
<style>
  :root {
    --backdrop: #8a8a8a;
    --rose: #b95e5e;
    --rose-deep: #a85252;
    --rose-faint: #b35959;
    --paper: #ffffff;
    --ink-gray: #6b6b6d;
    --ink-light: #8d8d90;
    --on-rose: #fbeeee;
  }
  * { margin: 0; padding: 0; box-sizing: border-box; }
  html, body { width: 1200px; height: 1200px; overflow: hidden; }
  body {
    background: var(--backdrop);
    display: flex; align-items: center; justify-content: center;
    font-family: "Montserrat", sans-serif;
  }
  .folder-spread {
    width: 1100px; height: 800px;
    display: flex;
    box-shadow: 0 10px 30px rgba(0,0,0,.25);
  }
  .panel { width: 50%; height: 100%; position: relative; }
  .panel--back { background: var(--rose); overflow: hidden; }
  .panel--front { background: var(--paper); }

  .back-emblem {
    position: absolute; left: 120px; top: 160px;
    width: 300px; height: 300px; border-radius: 50%;
    background: var(--rose-faint);
    box-shadow: inset 2px 2px 4px rgba(0,0,0,.08);
  }

  .contact-bar {
    position: absolute; left: 40px; right: 30px; bottom: 52px;
    display: flex; align-items: flex-start; gap: 26px;
    color: var(--on-rose); font-size: 10px; line-height: 1.45;
  }
  .contact-item { display: flex; align-items: center; gap: 7px; white-space: nowrap; }
  .contact-item--address { align-items: flex-start; }
  .contact-item svg { flex: none; }
  .icon-dot { width: 11px; height: 11px; border-radius: 50%; background: var(--on-rose); flex: none; }

  .brand {
    position: absolute; left: 50%; top: 330px;
    transform: translateX(-50%);
    text-align: center;
  }
  .brand-mark {
    width: 26px; height: 26px; border-radius: 50%;
    background: var(--rose); margin: 0 auto 14px;
  }
  .brand-title {
    font-family: "Cormorant Garamond", serif;
    color: var(--rose-deep); font-size: 16px; letter-spacing: 3px;
    text-align: left; margin-left: 6px;
  }
  .brand-name {
    font-family: "Cormorant Garamond", serif; font-weight: 400;
    color: var(--ink-gray); font-size: 62px; line-height: 1; white-space: nowrap;
  }
  .brand-specialty {
    margin-top: 10px; color: var(--ink-light);
    font-size: 13px; letter-spacing: 1.2px; white-space: nowrap;
  }
</style>
</head>
<body>
  <main class="folder-spread">
    <section class="panel panel--back">
      <div class="back-emblem" aria-hidden="true"></div>
      <div class="contact-bar">
        <div class="contact-item"><span class="icon-dot"></span>+55 (11) 3456-7821</div>
        <div class="contact-item">
          <svg width="12" height="9" viewBox="0 0 12 9"><rect x="0.5" y="0.5" width="11" height="8" rx="1" fill="var(--on-rose)"/><path d="M0.8 1 L6 5 L11.2 1" fill="none" stroke="var(--rose)" stroke-width="1"/></svg>
          contato@claramendes.med.br
        </div>
        <div class="contact-item contact-item--address">
          <svg width="10" height="14" viewBox="0 0 10 14"><path d="M5 0 C2.2 0 0 2.2 0 5 C0 8.5 5 14 5 14 C5 14 10 8.5 10 5 C10 2.2 7.8 0 5 0 Z" fill="var(--on-rose)"/><circle cx="5" cy="5" r="1.8" fill="var(--rose)"/></svg>
          <span>Rua das Acácias, 245<br>Jardim Paulista<br>01415-000 - São Paulo / SP</span>
        </div>
      </div>
    </section>
    <section class="panel panel--front">
      <div class="brand">
        <div class="brand-mark" aria-hidden="true"></div>
        <div class="brand-title">DRA.</div>
        <div class="brand-name">Clara Mendes</div>
        <div class="brand-specialty">OTORRINOLARINGOLOGISTA | RINOPLASTIA</div>
      </div>
    </section>
  </main>
</body>
</html>
```